make a fireworks website

we are manufacturer of fireworks in Asia.
we need a HD fireworks website for showing product to all world customers.
we also need an register for member system,location, forum,products..etc
I added my Logo for the company.
brightpeonyhall.com.hk

and please message me if you have
any question.
here some example of website:
http://www.lanternmoth.com/
http://www.korvelmist.com/
http://www.tindle-orbwick.co.uk/
http://www.pemberlyspark.co.uk/

```html
<!DOCTYPE html>
<html lang="en">
<head>
<meta charset="utf-8">
<title>brightpeonyhall.com.hk – Fireworks Night</title>
<link rel="stylesheet" href="https://fonts.googleapis.com/css2?family=Josefin+Sans:wght@400;600&family=Michroma&family=Great+Vibes&family=Roboto:wght@400;500&family=Arimo:wght@400;700&display=swap">
<style>
  :root {
    --black: #000;
    --ink: #222;
    --white: #fff;
    --purple: #8a3fa8;
    --purple-dark: #6a2e8e;
    --magenta: #c93aa8;
    --card: #e2e2e2;
    --panel-top: #ececec;
    --footer-top: #161616;
    --footer-bottom: #262626;
    --fire-gold: #f3c93a;
    --fire-orange: #c9631e;
    --fire-red: #7a1e2e;
  }
  * { box-sizing: border-box; margin: 0; padding: 0; }
  html, body { width: 1200px; height: 1194px; overflow: hidden; background: var(--black); }
  body { position: relative; font-family: "Arimo", Arial, sans-serif; color: var(--white); }

  .site-header { position: absolute; left: 0; top: 0; width: 1200px; height: 122px; }
  .brand { position: absolute; left: 138px; top: 46px; display: flex; align-items: center; gap: 10px;
    font-family: "Roboto", sans-serif; font-weight: 500; font-size: 19px; color: var(--white); }
  .brand-dot { width: 26px; height: 26px; border-radius: 50%; background: var(--magenta); }
  .main-nav { position: absolute; left: 430px; top: 58px; display: flex; align-items: center; }
  .main-nav a { font-family: "Roboto", sans-serif; font-size: 13.5px; font-weight: 500; color: var(--white);
    text-decoration: none; letter-spacing: 0.2px; margin-right: 34px; }
  .main-nav a.is-active { background: var(--purple); padding: 8px 14px; margin-right: 24px; }

  .hero { position: absolute; left: 0; top: 122px; width: 1200px; height: 442px; }
  .hero-visual { position: absolute; inset: 0;
    background:
      radial-gradient(circle at 735px 280px, #fff6d0 0, var(--fire-gold) 40px, rgba(210,140,40,.75) 120px, rgba(120,40,50,.45) 230px, rgba(0,0,0,0) 330px),
      radial-gradient(circle at 1010px 160px, rgba(220,120,40,.5) 0, rgba(0,0,0,0) 150px),
      var(--black); }
  .hero-tag { position: absolute; left: 138px; top: 87px; width: 323px; height: 58px; border-radius: 4px;
    background: linear-gradient(90deg, rgba(40,40,40,.95), rgba(40,40,40,.7) 80%, rgba(40,40,40,0));
    font-family: "Michroma", sans-serif; font-size: 34px; color: var(--white); padding: 6px 0 0 16px; }
  .hero-title { position: absolute; left: 134px; top: 150px; font-family: "Great Vibes", cursive;
    font-size: 142px; line-height: 1; color: transparent; -webkit-text-stroke: 1.5px #cfcfcf; }
  .register-btn { position: absolute; left: 138px; top: 360px; width: 163px; height: 30px; border-radius: 6px;
    background: linear-gradient(var(--purple), var(--purple-dark)); color: var(--white);
    font-family: "Roboto", sans-serif; font-size: 19px; text-align: center; line-height: 30px; text-decoration: none; }

  .store-panel { position: absolute; left: 138px; top: 564px; width: 923px; height: 408px; border-radius: 8px;
    background: var(--white); padding: 5px; }
  .store-inner { position: relative; height: 100%; border-radius: 6px;
    background: linear-gradient(var(--panel-top), var(--white) 140px); color: var(--ink); }
  .section-title { position: absolute; font-family: "Josefin Sans", sans-serif; font-size: 23px; letter-spacing: 1.2px; color: #111; }
  .categories-title { left: 12px; top: 22px; }
  .featured-title { left: 252px; top: 25px; }
  .category-list { position: absolute; left: 12px; top: 70px; list-style: none; }
  .category-list li { font-family: "Roboto", sans-serif; font-size: 13px; letter-spacing: .4px; height: 25.9px; color: #222; padding-left: 13px; position: relative; }
  .category-list li::before { content: ""; position: absolute; left: 1px; top: 5px; border-left: 3px solid #777;
    border-top: 2.5px solid transparent; border-bottom: 2.5px solid transparent; }
  .product-card { position: absolute; top: 63px; width: 198px; height: 270px; border-radius: 8px; background: var(--card); }
  .product-photo { position: absolute; left: 17px; top: 21px; width: 167px; height: 148px; border-radius: 8px;
    background: radial-gradient(circle at 50% 55%, #d9a0b8 0, #c6c6e6 35%, #fff 70%); }
  .product-price { position: absolute; left: 23px; top: 180px; font-family: "Arimo", sans-serif; font-size: 25px; color: #222; }
  .add-btn { position: absolute; left: 22px; top: 212px; width: 81px; height: 23px; border-radius: 4px; background: var(--magenta);
    color: var(--white); font-size: 10px; font-weight: 700; text-align: center; line-height: 23px; letter-spacing: .3px; text-decoration: none; }
  .details-link { position: absolute; left: 117px; top: 218px; font-size: 10px; font-weight: 700; color: #222; text-decoration: underline; }

  .site-footer { position: absolute; left: 0; top: 992px; width: 1200px; height: 169px;
    background: linear-gradient(var(--footer-top), var(--footer-bottom)); }
  .footer-links { position: absolute; top: 31px; list-style: none; }
  .footer-links li { font-size: 13px; height: 20.3px; padding-left: 12px; position: relative; }
  .footer-links li::before { content: ""; position: absolute; left: 0; top: 5px; border-left: 3px solid #ddd;
    border-top: 3px solid transparent; border-bottom: 3px solid transparent; }
  .footer-links a { color: var(--white); text-decoration: none; }
  .footer-map { position: absolute; left: 527px; top: 21px; width: 213px; height: 130px;
    background: linear-gradient(135deg, #ece6cf, #e3e0d8 50%, #d8dce6); border: 1px solid #fff; }
  .footer-brand { position: absolute; left: 820px; top: 64px; display: flex; align-items: center; gap: 10px;
    font-family: "Roboto", sans-serif; font-weight: 500; font-size: 19px; color: var(--white); }
  .copyright-bar { position: absolute; left: 0; top: 1161px; width: 1200px; height: 33px;
    background: linear-gradient(var(--purple), var(--purple-dark)); text-align: center; font-size: 11.5px; line-height: 33px; }
</style>
</head>
<body>
  <header class="site-header">
    <div class="brand"><span class="brand-dot"></span>brightpeonyhall.com.hk</div>
    <nav class="main-nav">
      <a href="#" class="is-active">HOME</a>
      <a href="#">LOCATIONS</a>
      <a href="#">OUR PRODUCTS</a>
      <a href="#">OFFERS</a>
      <a href="#">MAKE&nbsp; FIREWORKS</a>
      <a href="#">ABOUT US</a>
    </nav>
  </header>

  <section class="hero">
    <div class="hero-visual" role="img" aria-label="Large golden firework burst exploding in a dark night sky"></div>
    <div class="hero-tag">Fireworks</div>
    <div class="hero-title">Night</div>
    <a href="#" class="register-btn">REGISTER NOW</a>
  </section>

  <main class="store-panel">
    <div class="store-inner">
      <h2 class="section-title categories-title">All Categories</h2>
      <ul class="category-list">
        <li>Pro Barrages</li>
        <li>Single Ignition Barrages</li>
        <li>Cake Barrages</li>
        <li>Display Kits</li>
        <li>Rockets</li>
        <li>Clearance and Offers</li>
        <li>Roman Candles</li>
        <li>Catherine Wheels</li>
        <li>Quiet Fireworks</li>
        <li>Wedding Fireworks</li>
        <li>Clearance and Offers</li>
        <li>Catherine Wheels</li>
      </ul>

      <h2 class="section-title featured-title">Featured Products</h2>
      <article class="product-card" style="left:254px">
        <div class="product-photo" role="img" aria-label="Assorted firework boxes and cakes in a colourful pile"></div>
        <div class="product-price">$42.00</div>
        <a href="#" class="add-btn">ADD TO CART</a>
        <a href="#" class="details-link">DETAILS</a>
      </article>
      <article class="product-card" style="left:474px">
        <div class="product-photo" role="img" aria-label="Rocket selection pack with assorted fountains"></div>
        <div class="product-price">$42.00</div>
        <a href="#" class="add-btn">ADD TO CART</a>
        <a href="#" class="details-link">DETAILS</a>
      </article>
      <article class="product-card" style="left:692px">
        <div class="product-photo" role="img" aria-label="Assorted fountains and roman candles"></div>
        <div class="product-price">$42.00</div>
        <a href="#" class="add-btn">ADD TO CART</a>
        <a href="#" class="details-link">DETAILS</a>
      </article>
    </div>
  </main>

  <footer class="site-footer">
    <ul class="footer-links" style="left:146px">
      <li><a href="#">Home</a></li>
      <li><a href="#">Locations</a></li>
      <li><a href="#">Our Products</a></li>
      <li><a href="#">Offers</a></li>
      <li><a href="#">Make&nbsp; Fireworks</a></li>
      <li><a href="#">Contact Us</a></li>
    </ul>
    <ul class="footer-links" style="left:324px">
      <li><a href="#">Home</a></li>
      <li><a href="#">Locations</a></li>
      <li><a href="#">Our Products</a></li>
      <li><a href="#">Offers</a></li>
      <li><a href="#">Make&nbsp; Fireworks</a></li>
      <li><a href="#">Contact Us</a></li>
    </ul>
    <div class="footer-map" role="img" aria-label="Street map showing the store location"></div>
    <div class="footer-brand"><span class="brand-dot"></span>brightpeonyhall.com.hk</div>
  </footer>
  <div class="copyright-bar">Copyright © 2014 Halvern Ridge Company. All rights reserved.</div>
</body>
</html>
```